b-ryx design for startup inpection service

building and pest inspections what i had in mind was b-ryx in large print with prepurchase in small print directly under it and the small tm (tradmark) .Within the C I would like an eye but I don't want to take away from the C so maybe the eye would be done in a fine line?I would also like the Building and Pest inspections to be prominent and large .Have no idea of colors but do like black orange and silver

Target Market(s)

home buyers and realestate agents

Industry/Entity Type

Building

Contact Information for Business Card

b-ryx prepurchase, Phone 0413926058, fax 02 93514770, email b-ryx@mailnest.com.au ,building and pest inspections

Font styles to use
Sans Serif

Requirements
Must have
• bold color
• simple layout
• bold color
• uncluttered layout
Should not have
• contact details the same size as Building and Pest Inspections

```html
<!DOCTYPE html>
<html lang="en">
<head>
<meta charset="utf-8">
<title>b-ryx prepurchase – business card</title>
<link href="https://fonts.googleapis.com/css2?family=PT+Sans+Narrow:wght@700&family=Fira+Sans:wght@400;500&display=swap" rel="stylesheet">
<style>
  :root {
    --stage: #7a0d0d;
    --card: #f3f3f3;
    --brand-blue: #1c4587;
    --brand-red: #d63a2a;
    --strip: #e3e4e6;
    --ink: #3d4148;
    --ink-soft: #4a4e55;
  }
  * { margin: 0; padding: 0; box-sizing: border-box; }
  html, body {
    width: 1200px; height: 970px; overflow: hidden;
    background: var(--stage);
  }
  .card {
    position: absolute; left: 345px; top: 70px;
    width: 513px; height: 830px;
    background: var(--card);
    box-shadow: 0 8px 30px rgba(0,0,0,.55);
    font-family: "Fira Sans", sans-serif;
  }
  .side-band {
    position: absolute; left: 0; top: 0;
    width: 56px; height: 528px;
    background: var(--brand-blue);
  }
  .corner-block {
    position: absolute; left: 0; bottom: 0;
    width: 56px; height: 85px;
    background: var(--brand-red);
  }
  .title-bar {
    position: absolute; left: 186px; top: 124px;
    width: 327px; height: 57px;
    background: var(--brand-blue);
    color: #fff;
    font-family: "PT Sans Narrow", sans-serif;
    font-weight: 700; font-size: 37px;
    line-height: 57px;
    padding-left: 34px;
    letter-spacing: -0.2px;
  }
  .tagline {
    position: absolute; right: 40px; top: 184px;
    font-size: 18px; color: var(--ink);
  }
  .brand-mark {
    position: absolute; left: 90px; top: 388px;
    display: flex; align-items: center; gap: 18px;
  }
  .brand-dot {
    width: 56px; height: 56px; border-radius: 50%;
    background: var(--brand-blue);
  }
  .brand-name {
    font-size: 64px; font-weight: 500;
    color: var(--brand-blue); line-height: 1;
  }
  .contact {
    position: absolute; left: 0; width: 449px; height: 50px;
    background: var(--strip);
    display: flex; align-items: center;
    font-size: 24px; color: var(--ink-soft);
    letter-spacing: 0.3px;
  }
  .contact svg { position: absolute; left: 68px; width: 18px; height: 18px; }
  .contact span { position: absolute; left: 109px; }
  .contact-phone { top: 530px; }
  .contact-fax { top: 611px; }
  .contact-email { top: 692px; }
</style>
</head>
<body>
  <main class="card">
    <div class="side-band"></div>
    <div class="corner-block"></div>

    <h1 class="title-bar">b-ryx prepurchase</h1>
    <p class="tagline">Building and Pest inspections</p>

    <div class="brand-mark">
      <div class="brand-dot"></div>
      <div class="brand-name">b-ryx</div>
    </div>

    <div class="contact contact-phone">
      <svg viewBox="0 0 18 18" aria-hidden="true"><path d="M6 3 Q3 9 6 15 L8 13.5 Q6.5 9 8 4.5 Z" fill="#2b3a55"/></svg>
      <span>0413926058</span>
    </div>
    <div class="contact contact-fax">
      <svg viewBox="0 0 18 18" aria-hidden="true" fill="none" stroke="#2b3a55" stroke-width="1.6"><rect x="4" y="2" width="10" height="7"/><rect x="1.5" y="9" width="15" height="7"/><line x1="5" y1="12.5" x2="13" y2="12.5"/></svg>
      <span>02 93514770</span>
    </div>
    <div class="contact contact-email">
      <svg viewBox="0 0 18 18" aria-hidden="true" fill="none" stroke="#2b3a55" stroke-width="1.6"><rect x="1.5" y="4" width="15" height="10"/><path d="M1.5 4 L9 10 L16.5 4"/></svg>
      <span>b-ryx@mailnest.com.au</span>
    </div>
  </main>
</body>
</html>
```